Corvale Real Estate

I manage 2 firms. The first one is Pelmora and the logo is in blue (see the file) but i need a design for my business card for the second firm called CORVALE IMMOBILIER. This one is in charge of Real estate developer.

Colors
3176b5

```html
<!DOCTYPE html>
<html lang="en">
<head>
<meta charset="UTF-8">
<title>Corvale Immobilier – Business Card</title>
<link rel="stylesheet" href="https://fonts.googleapis.com/css2?family=Montserrat:wght@700&family=Oswald:wght@600&family=Work+Sans:wght@400&display=swap">
<style>
  :root {
    --brand-blue: #3176b5;
    --page-bg: #151515;
    --card-bg: #1f1f1f;
    --card-bg-light: #2a2a2a;
    --text-light: #f2f2f2;
  }
  * { margin: 0; padding: 0; box-sizing: border-box; }
  html, body {
    width: 1200px; height: 900px; overflow: hidden;
    background: var(--page-bg);
  }
  .canvas {
    position: relative; width: 1200px; height: 900px;
    display: flex; flex-direction: column; align-items: center; justify-content: center;
    gap: 36px;
  }
  .card {
    position: relative; width: 720px; height: 405px;
    background: linear-gradient(135deg, var(--card-bg) 0%, var(--card-bg) 55%, var(--card-bg-light) 100%);
    box-shadow: 0 10px 30px rgba(0,0,0,0.55);
  }
  /* Front */
  .card-front { display: flex; align-items: center; justify-content: center; }
  .brand-wordmark {
    display: flex; align-items: center; gap: 18px;
    font-family: "Montserrat", sans-serif; font-weight: 700;
    color: var(--brand-blue);
  }
  .brand-square { width: 24px; height: 24px; background: var(--brand-blue); flex: none; }
  .brand-name { display: flex; flex-direction: column; line-height: 1.05; }
  .brand-name-main { font-size: 40px; letter-spacing: 6px; }
  .brand-name-sub { font-size: 18px; letter-spacing: 8.5px; }
  /* Back */
  .card-back { font-family: "Work Sans", sans-serif; color: var(--text-light); }
  .details {
    position: absolute; left: 0; right: 0; top: 148px;
    display: flex; align-items: flex-start; justify-content: center; gap: 22px;
  }
  .identity { text-align: right; }
  .person-name {
    font-family: "Oswald", sans-serif; font-weight: 600;
    font-size: 36px; line-height: 1; letter-spacing: 0.5px;
    color: var(--brand-blue); text-transform: uppercase; white-space: nowrap;
  }
  .person-role { margin-top: 8px; font-size: 17px; letter-spacing: 1px; }
  .divider {
    width: 2px; height: 74px; background: var(--brand-blue); flex: none;
  }
  .contact-list {
    list-style: none; padding-top: 2px;
    font-size: 15px; letter-spacing: 0.8px;
  }
  .contact-item { display: flex; align-items: center; gap: 10px; height: 24px; white-space: nowrap; }
  .contact-icon { width: 12px; height: 12px; flex: none; }
  .address {
    position: absolute; left: 0; right: 0; bottom: 44px; text-align: center;
    font-size: 17px; letter-spacing: 1.5px;
  }
</style>
</head>
<body>
<main class="canvas">
  <section class="card card-front">
    <div class="brand-wordmark">
      <span class="brand-square"></span>
      <span class="brand-name">
        <span class="brand-name-main">CORVALE</span>
        <span class="brand-name-sub">IMMOBILIER</span>
      </span>
    </div>
  </section>

  <section class="card card-back">
    <div class="details">
      <div class="identity">
        <h1 class="person-name">Adrien Moreau</h1>
        <p class="person-role">Founder</p>
      </div>
      <span class="divider"></span>
      <ul class="contact-list">
        <li class="contact-item">
          <svg class="contact-icon" viewBox="0 0 16 16" fill="none" stroke="#3176b5" stroke-width="1.6"><path d="M4 1.5 L6.5 5 L5 6.5 C6 8.8 7.2 10 9.5 11 L11 9.5 L14.5 12 L13 14.5 C7 14 2 9 1.5 3 Z"/></svg>
          <span>214-555-0178</span>
        </li>
        <li class="contact-item">
          <svg class="contact-icon" viewBox="0 0 16 16" fill="none" stroke="#3176b5" stroke-width="1.6"><rect x="1.5" y="3.5" width="13" height="9"/><path d="M1.5 3.5 L8 9 L14.5 3.5"/></svg>
          <span>hello@corvaleimmobilier.com</span>
        </li>
        <li class="contact-item">
          <svg class="contact-icon" viewBox="0 0 16 16" fill="none" stroke="#3176b5" stroke-width="1.4"><circle cx="8" cy="8" r="6.5"/><ellipse cx="8" cy="8" rx="3" ry="6.5"/><path d="M1.5 8 H14.5"/></svg>
          <span>corvaleimmobilier.com</span>
        </li>
      </ul>
    </div>
    <p class="address">418 N. Bishop Avenue #205 Dallas, TX&nbsp; 75208</p>
  </section>
</main>
</body>
</html>
```